Kestrel Photography Business Card

I need a business card designed for a photography business based in Perth, Western Australia called Kestrel Photography.

We specialise in wedding, event photography and portrait photography.

The business card must borrow the style of the attached logo.

The hex codes for the colours in the logo are:
#ED1D85 - Pink
#89C23E - Green
#37282F - Black

The name on the card will be:
Name: Torvane
Phone: 0417395286
Website: www.kestrelphotography.example.au
Facebook: kestrelphotography

I am open and happy to accept creative concepts.

I’d like some space at the back for writing notes and appointment details.

```html
<!DOCTYPE html>
<html lang="en">
<head>
<meta charset="utf-8">
<title>Kestrel Photography Business Card</title>
<link href="https://fonts.googleapis.com/css2?family=Questrial&display=swap" rel="stylesheet">
<style>
  :root {
    --pink: #ED1D85;
    --pink-deep: #E0157A;
    --green: #89C23E;
    --black: #37282F;
    --paper: #FFFFFF;
    --backdrop: #EDEDEE;
  }
  * { margin: 0; padding: 0; box-sizing: border-box; }
  html, body { width: 1200px; height: 900px; overflow: hidden; }
  body {
    background: var(--backdrop);
    font-family: "Questrial", "Helvetica Neue", Arial, sans-serif;
    position: relative;
  }
  .card {
    position: absolute;
    top: 290px;
    width: 540px;
    height: 310px;
    overflow: hidden;
    box-shadow: 0 2px 6px rgba(0,0,0,0.12);
  }
  /* Front */
  .card--front { left: 620px; background: var(--paper); }
  .front__mark {
    position: absolute;
    left: 50%; top: 26px;
    width: 84px; height: 84px;
    margin-left: -42px;
    border-radius: 50%;
    background: var(--pink);
  }
  .front__wordmark {
    position: absolute;
    left: 0; right: 0; top: 130px;
    text-align: center;
    font-size: 17px;
    letter-spacing: 0.62em;
    color: var(--black);
    text-transform: uppercase;
    padding-left: 0.62em;
  }
  .front__details {
    position: absolute;
    left: 0; right: 0; top: 168px;
    text-align: center;
    color: var(--black);
    text-transform: uppercase;
    font-size: 13px;
    letter-spacing: 0.12em;
    line-height: 1.35;
  }
  .front__name {
    color: var(--pink);
    font-size: 19px;
    letter-spacing: 0.08em;
    margin-bottom: 2px;
  }
  .front__label { color: var(--green); }
  .front__rule {
    position: absolute;
    left: 0; right: 0; bottom: 18px;
    height: 2px;
    background: var(--green);
  }
  .front__band {
    position: absolute;
    left: 0; right: 0; bottom: 0;
    height: 13px;
    background: var(--pink);
  }
  /* Back */
  .card--back { left: 40px; background: var(--pink); }
  .back__pattern {
    position: absolute;
    inset: 0;
    background: radial-gradient(circle at 55% 30%, var(--pink-deep) 0%, var(--pink) 70%);
  }
  .back__mark {
    position: absolute;
    left: 50%; top: 22px;
    width: 70px; height: 70px;
    margin-left: -35px;
    border-radius: 50%;
    background: var(--paper);
  }
  .back__wordmark {
    position: absolute;
    left: 0; right: 0; top: 100px;
    text-align: center;
    color: var(--paper);
    font-size: 11px;
    letter-spacing: 0.5em;
    text-transform: uppercase;
  }
  .back__notes {
    position: absolute;
    left: 40px; right: 40px; top: 140px;
    height: 130px;
    background: var(--paper);
    border: 2px solid var(--green);
    border-radius: 8px;
  }
</style>
</head>
<body>
  <section class="card card--back" aria-label="Business card back">
    <div class="back__pattern" role="img" aria-label="Faint pink leaf pattern"></div>
    <div class="back__mark"></div>
    <p class="back__wordmark">Kestrel Photography</p>
    <div class="back__notes" aria-label="Space for notes and appointment details"></div>
  </section>

  <section class="card card--front" aria-label="Business card front">
    <div class="front__mark"></div>
    <h1 class="front__wordmark">Kestrel Photography</h1>
    <div class="front__details">
      <p class="front__name">Torvane</p>
      <p>0417395286</p>
      <p>www.kestrelphotography.example.au</p>
      <p><span class="front__label">Facebook:</span> kestrelphotography</p>
    </div>
    <div class="front__rule"></div>
    <div class="front__band"></div>
  </section>
</body>
</html>
```